Most captivating card ever!

Life Coach - Professional Adventurer - Entrepreneur
I need the worlds most amazing business card for my personal brand. This business card will mostly be used to give to prospective clients for life coaching and business coaching.
Be creative, be adventurous. It needs to stand out. Make people say.. I need this guy!
My background is as an entrepreneur and professional adventurer undertaking extreme expeditions. I am now moving into life coaching.
No specific design ideas, so you have full creativity. Show me your best.
Industry/Entity Type
Life Coaching
Contact Information for Business Card
Mark Dellow
meetmark.com.au
0458260913
Colors
Designer to choose colors to be used in the design.
Look and feel

```html
<!DOCTYPE html>
<html lang="en">
<head>
<meta charset="utf-8">
<title>Mark Dellow – Business Card</title>
<link rel="stylesheet" href="https://fonts.googleapis.com/css2?family=Sorts+Mill+Goudy&family=Arimo&display=swap">
<style>
  :root {
    --card-bg: #333333;
    --banner-white: #ffffff;
    --accent-yellow: #ffff00;
    --accent-teal: #13c4b6;
    --ink-dark: #333333;
    --ink-light: #ffffff;
    --ink-black: #000000;
  }
  html, body {
    margin: 0;
    padding: 0;
    width: 1200px;
    height: 640px;
    overflow: hidden;
    background: var(--card-bg);
  }
  .card {
    position: relative;
    width: 1200px;
    height: 640px;
    background: var(--card-bg);
    overflow: hidden;
  }
  .card-graphics {
    position: absolute;
    inset: 0;
  }
  .brand-name {
    position: absolute;
    left: 30px;
    top: 80px;
    width: 260px;
    margin: 0;
    font-family: "Sorts Mill Goudy", serif;
    font-size: 42px;
    line-height: 50px;
    font-weight: 400;
    color: var(--ink-dark);
    white-space: nowrap;
  }
  .owner-name {
    position: absolute;
    left: 460px;
    top: 220px;
    margin: 0;
    font-family: "Sorts Mill Goudy", serif;
    font-weight: 400;
    font-size: 64px;
    line-height: 80px;
    color: var(--ink-light);
  }
  .owner-roles {
    position: absolute;
    left: 464px;
    top: 306px;
    margin: 0;
    font-family: "Sorts Mill Goudy", serif;
    font-size: 30px;
    line-height: 40px;
    color: var(--ink-light);
    white-space: nowrap;
  }
  .contact-text {
    position: absolute;
    top: 510px;
    margin: 0;
    font-family: "Arimo", sans-serif;
    font-size: 34px;
    line-height: 48px;
    color: var(--ink-black);
    white-space: nowrap;
  }
  .contact-web { left: 538px; }
  .contact-phone { left: 944px; }
</style>
</head>
<body>
<main class="card">
  <svg class="card-graphics" width="1200" height="640" viewBox="0 0 1200 640" aria-hidden="true">
    <polygon class="banner" points="0,26 290,26 390,105 290,186 0,186" fill="var(--banner-white)"/>
    <polygon class="stripe-yellow" points="512,0 540,0 74,640 46,640" fill="var(--accent-yellow)"/>
    <polygon class="stripe-teal" points="545,0 561,0 93,640 77,640" fill="var(--accent-teal)"/>
    <polygon class="stripe-yellow" points="568,0 590,0 120,640 98,640" fill="var(--accent-yellow)"/>
    <path class="contact-bar" d="M446,501 H1200 V568 H446 Q430,568 430,552 V517 Q430,501 446,501 Z" fill="var(--accent-yellow)"/>
    <g class="icon-web">
      <circle cx="490" cy="534" r="27" fill="var(--ink-black)"/>
      <g fill="none" stroke="var(--accent-yellow)" stroke-width="2.2">
        <circle cx="490" cy="534" r="13"/>
        <ellipse cx="490" cy="534" rx="6" ry="13"/>
        <line x1="490" y1="521" x2="490" y2="547"/>
        <line x1="477" y1="534" x2="503" y2="534"/>
        <line x1="479" y1="527" x2="501" y2="527"/>
        <line x1="479" y1="541" x2="501" y2="541"/>
      </g>
    </g>
    <g class="icon-phone">
      <rect x="854" y="507" width="53" height="53" rx="9" fill="var(--ink-black)"/>
      <path d="M868,519 L874,517 L879,527 L875,531 Q878,539 886,543 L890,539 L900,544 L898,550 Q894,553 888,551 Q870,544 864,527 Q863,522 868,519 Z" fill="var(--accent-yellow)"/>
    </g>
  </svg>

  <p class="brand-name">Mark Dellow</p>
  <h1 class="owner-name">Mark Dellow</h1>
  <p class="owner-roles">Life Coach - Professional Adventurer - Entrepreneur</p>
  <p class="contact-text contact-web">meetmark.com.au</p>
  <p class="contact-text contact-phone">0458260913</p>
</main>
</body>
</html>
```